依頼詳細
チラシの用途としては、店前の歩行者にチラシの存在に気付いてもらい持って帰っていただく。お店の半径500mの住居へのポスティング等を考えております。

直接お電話での注文とトークルの友達登録からの注文も期待したいです。
記載項目
過去作成したチラシを添付します。

情報の変更はありませんが「柚木坂の焼きそばパン」という記載はロゴでクリアーになっているため、除いてください。
サイズ
A4
ページ数
片面
希望イメージ
シンプル 複雑
単色 カラフル
暗い 明るい
日常 高級
遊び心 厳粛
未来的 伝統的
女性的 男性的
希望する色
赤系、黄・オレンジ系、茶系
納品ファイル
• イラストレーター形式 (.ai)
補足説明
今回は商品写真の変更により新たにチラシの制作です。
既存のチラシはスタッフが作成しましたが、時間もかかったため今回は依頼となりました。
営業時間等変更があるため、イラストレーター形式での納品希望です。
■ 選んだ理由

余白の使い方、キャッチになるタイトルの色など全体のバランスがすっきりして清潔な印象を受け、食品のチラシとして最適と思いました。

■ 提案者全員のお礼・コメント

この度は多くの方のご提案非常にうれしく思います。誠にありがとうございました。

```html
<!DOCTYPE html>
<html lang="ja">
<head>
<meta charset="utf-8">
<title>柚木坂 焼きそばパン TAKE OUT</title>
<link rel="stylesheet" href="https://fonts.googleapis.com/css2?family=Noto+Serif+JP:wght@700;900&family=Noto+Sans+JP:wght@400;700;900&family=Oswald:wght@600;700&family=Pacifico&family=Yuji+Syuku&display=swap">
<style>
  :root{
    --bg:#2a1a13;
    --bg-deep:#1c110c;
    --red:#c8161e;
    --gold:#f3dca0;
    --yellow:#f6d21c;
    --cream:#fff6df;
    --green:#2fae3c;
    --green-dark:#1f8a2c;
    --white:#ffffff;
    --ink:#2a1a13;
    --wood-1:#8a5a33;
    --wood-2:#c48a55;
  }
  *{margin:0;padding:0;box-sizing:border-box}
  html,body{width:848px;height:1200px;overflow:hidden;background:var(--bg)}
  .flyer{
    position:relative;width:848px;height:1200px;overflow:hidden;
    background:radial-gradient(ellipse at 50% 30%, #3a2519 0%, var(--bg) 55%, var(--bg-deep) 100%);
    font-family:"Noto Sans JP",sans-serif;color:var(--white);
  }
  .maker-tag{position:absolute;left:0;top:30px;width:250px;height:46px}
  .maker-tag svg{position:absolute;left:0;top:0}
  .maker-tag span{position:absolute;left:44px;top:11px;font-weight:900;font-size:16px;line-height:24px;color:var(--white);white-space:nowrap;letter-spacing:1px}
  .headline{position:absolute;left:90px;top:95px;width:480px;text-align:center}
  .headline .lead{font-family:"Noto Serif JP",serif;font-weight:900;font-size:34px;color:var(--gold);letter-spacing:3px;white-space:nowrap}
  .headline .takeout{display:flex;align-items:center;justify-content:center;gap:12px;margin-top:2px;font-family:"Oswald",sans-serif;font-weight:700;font-size:80px;line-height:1;color:var(--gold);letter-spacing:2px;white-space:nowrap}
  .headline .only{font-family:"Pacifico",cursive;font-size:40px;line-height:1.4;color:var(--red);transform:rotate(-10deg);letter-spacing:0}
  .limit{position:absolute;left:120px;top:205px;display:flex;align-items:center;gap:12px;font-family:"Noto Serif JP",serif;font-weight:900;color:var(--gold);white-space:nowrap}
  .limit .day{font-size:28px;letter-spacing:2px}
  .limit .num{font-family:"Oswald",sans-serif;font-size:56px;line-height:1}
  .limit .num small{font-family:"Noto Serif JP",serif;font-size:28px}
  .limit .box{background:var(--red);color:var(--white);font-size:40px;line-height:1.3;padding:2px 12px;letter-spacing:4px}
  .brand{position:absolute;left:600px;top:45px;width:200px;display:flex;flex-direction:column;align-items:center;gap:10px}
  .brand .mark{width:100px;height:100px;border-radius:50%;background:var(--cream)}
  .brand .name{font-family:"Noto Serif JP",serif;font-weight:900;font-size:40px;line-height:1.1;color:var(--cream);letter-spacing:4px}
  .wood{position:absolute;left:0;top:600px;width:848px;height:280px;background:linear-gradient(180deg,var(--bg) 0%,var(--wood-1) 25%,var(--wood-2) 60%,var(--wood-1) 100%)}
  .photo{position:absolute;border-radius:46% 46% 40% 40%}
  .photo-tartar{left:28px;top:290px;width:400px;height:470px;background:radial-gradient(ellipse at 50% 45%,#b9d98a 0%,#d7a05a 35%,#a8652e 70%,rgba(80,45,20,0) 100%)}
  .photo-carrot{left:430px;top:380px;width:410px;height:400px;background:radial-gradient(ellipse at 50% 50%,#f0e2b6 0%,#e7a14c 40%,#a76a33 72%,rgba(80,45,20,0) 100%)}
  .price{position:absolute;width:100px;height:100px;border-radius:50%;background:var(--yellow);color:var(--ink);display:flex;flex-direction:column;align-items:center;justify-content:center;font-family:"Oswald",sans-serif;font-size:34px;line-height:1}
  .price small{font-family:"Noto Sans JP",sans-serif;font-size:12px;font-weight:700;margin-top:4px}
  .price-tartar{left:50px;top:290px}
  .price-carrot{left:715px;top:690px}
  .item-name{position:absolute;font-family:"Yuji Syuku",serif;font-size:40px;line-height:1.2;color:var(--white);text-shadow:0 2px 6px rgba(0,0,0,.6);white-space:nowrap}
  .name-carrot{left:510px;top:298px}
  .name-tartar{left:62px;top:670px}
  .ingredients{position:absolute;list-style:none;font-size:12px;line-height:1.6;font-weight:700;color:var(--white);display:grid;grid-template-columns:auto auto;gap:2px 18px;text-shadow:0 1px 3px rgba(0,0,0,.7);white-space:nowrap}
  .ingredients li::before{content:"● ";color:var(--yellow)}
  .ing-carrot{left:515px;top:360px}
  .ing-tartar{left:64px;top:730px}
  .order{position:absolute;left:62px;top:800px;width:430px;height:305px;background:var(--white);border-radius:10px;padding:18px 18px;color:var(--ink)}
  .order .ask{font-weight:900;font-size:20px;text-align:center;margin-bottom:14px;white-space:nowrap}
  .order .ask em{font-style:normal;color:var(--red)}
  .order .body{display:flex;gap:14px;align-items:flex-start}
  .order .info{flex:1;min-width:0}
  .order .account{display:flex;align-items:center;gap:8px;background:var(--green);color:var(--white);font-weight:900;font-size:17px;padding:8px 10px;border-radius:6px;white-space:nowrap}
  .order .account i{width:20px;height:20px;border-radius:4px;background:var(--white);display:block;flex:none}
  .order .friends{font-weight:900;font-size:17px;color:var(--green-dark);margin:12px 0 6px}
  .order .howto{font-size:11px;line-height:1.5}
  .order .id{display:inline-block;margin-top:12px;background:var(--green-dark);color:var(--white);border-radius:20px;padding:4px 18px;font-weight:700;font-size:16px}
  .order .scan-space{width:130px;height:130px;border:2px solid var(--green);border-radius:6px;flex:none}
  .shop{position:absolute;left:515px;top:930px;width:310px;color:var(--white)}
  .shop .title{display:flex;align-items:baseline;gap:10px;font-size:12px;font-weight:700;white-space:nowrap}
  .shop .title b{font-family:"Noto Serif JP",serif;font-size:28px;font-weight:900}
  .shop .row{display:flex;gap:12px;margin-top:12px;align-items:flex-start}
  .shop .tel{display:flex;align-items:center;gap:6px;font-family:"Oswald",sans-serif;font-size:22px;color:var(--yellow);white-space:nowrap}
  .shop .hours{border:1px solid var(--white);padding:4px 8px;font-size:11px;line-height:1.5;white-space:nowrap}
  .shop .hours b{display:block;background:var(--white);color:var(--ink);text-align:center;margin:-4px -8px 4px}
  .note{position:absolute;left:0;top:1138px;width:848px;text-align:center;font-size:15px;font-weight:700;color:var(--yellow);letter-spacing:1px;white-space:nowrap}
</style>
</head>
<body>
<main class="flyer">
  <div class="maker-tag">
    <svg width="250" height="46" viewBox="0 0 250 46" aria-hidden="true"><path d="M0 0H250L234 23L250 46H0Z" fill="var(--red)"/><circle cx="22" cy="23" r="9" fill="none" stroke="#fff" stroke-width="2.5"/></svg>
    <span>お好み焼き屋がつくった</span>
  </div>

  <header class="headline">
    <p class="lead">本気の焼きそばパン！</p>
    <p class="takeout"><span class="only">Only</span>TAKE OUT</p>
  </header>
  <p class="limit"><span class="day">一日それぞれ</span><span class="num">25<small>食</small></span><span class="box">限定</span></p>

  <div class="brand">
    <div class="mark"></div>
    <p class="name">柚木坂</p>
  </div>

  <div class="wood" role="img" aria-label="木目のテーブル"></div>
  <div class="photo photo-carrot" role="img" aria-label="キャロットラペを挟んだ焼きそばパンの写真"></div>
  <div class="photo photo-tartar" role="img" aria-label="タルタルキャベツとアボカド、トマトを挟んだ焼きそばパンの写真"></div>

  <div class="price price-tartar">¥700<small>(税別)</small></div>
  <div class="price price-carrot">¥650<small>(税別)</small></div>

  <h2 class="item-name name-carrot">キャロットラペ</h2>
  <ul class="ingredients ing-carrot">
    <li>特製パン</li><li>キャロットラペ</li>
    <li>柚木坂の焼きそば</li><li>アボカド</li>
    <li>特製ヨーグルトソース</li><li>パクチー</li>
  </ul>

  <h2 class="item-name name-tartar">タルタルキャベツ</h2>
  <ul class="ingredients ing-tartar">
    <li>特製パン</li><li>シャキシャキキャベツ</li>
    <li>柚木坂の焼きそば</li><li>自家製タルタル</li>
    <li>特製ソース</li><li>紅ショウガ</li>
  </ul>

  <section class="order">
    <p class="ask">ご注文は<em>トークル</em>または<em>お電話</em>で！</p>
    <div class="body">
      <div class="info">
        <p class="account"><i></i>トークル 公式アカウント</p>
        <p class="friends">ともだち募集中!!</p>
        <p class="howto">登録はIDから友だち追加でお願いします</p>
        <span class="id">@yuzu25pan</span>
      </div>
      <div class="scan-space"></div>
    </div>
  </section>

  <section class="shop">
    <p class="title">お好み焼き・焼きそば <b>柚木坂</b></p>
    <div class="row">
      <p class="tel"><svg width="20" height="20" viewBox="0 0 24 24" aria-hidden="true"><path d="M6.6 10.8a15 15 0 0 0 6.6 6.6l2.2-2.2a1 1 0 0 1 1-.25 11.4 11.4 0 0 0 3.6.57 1 1 0 0 1 1 1V20a1 1 0 0 1-1 1A17 17 0 0 1 3 4a1 1 0 0 1 1-1h3.5a1 1 0 0 1 1 1 11.4 11.4 0 0 0 .57 3.6 1 1 0 0 1-.25 1z" fill="var(--yellow)"/></svg>099-555-0182</p>
      <p class="hours"><b>営業時間</b>火 17:30〜22:30<br>水〜日 11:30〜14:00<br>定休日 月曜</p>
    </div>
  </section>

  <p class="note">個数限定商品のため、24時間受付のトークルからの注文をお勧めしています</p>
</main>
</body>
</html>
```